Vorel constructions

We are predominantly a residential home builder based in Melbourne, Victoria Australia. We construct houses, apartments, townhouses, multi-unit developments.

The name of the company is "Vorel Constructions"
My company believes in building unique construction projects mainly residential homes. The target customers are upmarket Melbourne residents/investors.

I want the brand name "Vorel" to be part of the logo. There's no need to put the word construction in the logo at this stage.

I would also like some ideas for a slogan e.g. "Just build it." or "We build quality homes." But I would like something unique and different for a slogan not the same old cliche.

vorelconstructions.example.com.au
e: tmelo@vorelconstructions.example.com.au
M: 0417305862
Address: 8/3 Fenwick Lane Ashvale VIC 3199

Director:Mr Dinesh Malarkodiyan

```html
<!DOCTYPE html>
<html lang="en">
<head>
<meta charset="utf-8">
<title>Vorel Constructions – Business Card</title>
<link rel="stylesheet" href="https://fonts.googleapis.com/css2?family=Questrial&family=Josefin+Sans:wght@600&display=swap">
<style>
  :root {
    --page-bg: #d9d9d7;
    --card-navy: #08083f;
    --card-navy-light: #1c1c5e;
    --accent-cyan: #1fb8e8;
    --text-white: #ffffff;
    --font-main: "Questrial", "Century Gothic", sans-serif;
    --font-title: "Josefin Sans", "Century Gothic", sans-serif;
  }
  * { margin: 0; padding: 0; box-sizing: border-box; }
  html, body {
    width: 1200px; height: 1000px; overflow: hidden;
    background: var(--page-bg);
  }
  .business-card {
    position: absolute; left: 139px; top: 136px;
    width: 903px; height: 578px;
    background: var(--card-navy);
    overflow: hidden;
    font-family: var(--font-main);
    color: var(--text-white);
  }
  .halftone-wave {
    position: absolute; left: 0; top: 130px; width: 903px; height: 448px;
    background:
      radial-gradient(ellipse 60% 45% at 75% 80%, rgba(60,60,130,0.55), transparent 70%),
      radial-gradient(ellipse 45% 40% at 20% 75%, rgba(50,50,120,0.5), transparent 70%),
      linear-gradient(180deg, transparent 0%, var(--card-navy-light) 100%);
  }
  .brand-block { position: absolute; left: 0; top: 0; width: 356px; height: 578px; }
  .brand-square {
    position: absolute; left: 206px; bottom: 106px;
    width: 28px; height: 28px; background: var(--accent-cyan);
  }
  .brand-name, .brand-slogan {
    position: absolute;
    writing-mode: vertical-rl;
    transform: rotate(180deg);
    white-space: nowrap;
    line-height: 1;
  }
  .brand-name {
    left: 252px; bottom: 106px;
    font-size: 40px; letter-spacing: 2px;
    color: var(--text-white);
  }
  .brand-slogan {
    left: 303px; bottom: 106px;
    font-size: 20px; letter-spacing: 0.5px;
    color: var(--accent-cyan);
  }
  .divider {
    position: absolute; left: 355px; top: 19px; height: 526px;
    border-left: 3px dotted var(--text-white);
  }
  .contact-person { position: absolute; left: 428px; top: 112px; }
  .person-name { font-size: 28px; letter-spacing: 0.3px; line-height: 1.2; }
  .person-role {
    margin-top: 10px; font-family: var(--font-title);
    font-weight: 600; font-size: 23px; letter-spacing: 0.5px; line-height: 1.2;
  }
  .contact-list { position: absolute; left: 383px; top: 224px; list-style: none; }
  .contact-item {
    display: flex; align-items: center; height: 45px;
    font-size: 27px; white-space: nowrap;
  }
  .contact-item.is-small { font-size: 23px; }
  .contact-icon { width: 30px; height: 30px; margin-right: 14px; flex: none; }
</style>
</head>
<body>
  <section class="business-card">
    <div class="halftone-wave" role="img" aria-label="Soft halftone dot wave pattern in navy tones"></div>

    <div class="brand-block">
      <div class="brand-square"></div>
      <div class="brand-name">Vorel constructions</div>
      <div class="brand-slogan">HOMES SHAPED LIKE YOU</div>
    </div>

    <div class="divider"></div>

    <div class="contact-person">
      <p class="person-name">Mr Dinesh Malarkodiyan</p>
      <p class="person-role">DIRECTOR</p>
    </div>

    <ul class="contact-list">
      <li class="contact-item">
        <svg class="contact-icon" viewBox="0 0 30 30"><path d="M15 3a7 7 0 0 0-7 7c0 5 7 15 7 15s7-10 7-15a7 7 0 0 0-7-7z" fill="#fff"/><circle cx="15" cy="10" r="2.6" fill="#08083f"/></svg>
        8/3 Fenwick Lane Ashvale VIC 3199
      </li>
      <li class="contact-item">
        <svg class="contact-icon" viewBox="0 0 30 30"><rect x="9" y="3" width="13" height="24" rx="2" fill="none" stroke="#fff" stroke-width="2.4"/><rect x="11.5" y="6.5" width="8" height="14" fill="#fff"/><circle cx="15.5" cy="23.5" r="1.3" fill="#fff"/></svg>
        0417305862
      </li>
      <li class="contact-item is-small">
        <svg class="contact-icon" viewBox="0 0 30 30"><path d="M3 12 15 4l12 8v14H3z M3 12l12 8 12-8" fill="none" stroke="#fff" stroke-width="2" stroke-linejoin="round"/></svg>
        tmelo@vorelconstructions.example.com.au
      </li>
      <li class="contact-item is-small">
        <svg class="contact-icon" viewBox="0 0 30 30"><rect x="6" y="6" width="18" height="13" fill="none" stroke="#fff" stroke-width="2"/><path d="M2 24h26l-3-4H5z" fill="none" stroke="#fff" stroke-width="2" stroke-linejoin="round"/></svg>
        vorelconstructions.example.com.au
      </li>
    </ul>
  </section>
</body>
</html>
```